Varneck Bidding Business Cards Design Needed

I need a business card design that is modern looking - double sided (maybe just my logo on the back, but open to suggestions) - the overall design is up to you. I want it to be easy to read - not over the top flashy. I already have a company logo which I uploaded so that needs to be used. The colors of my logo are the colors I want on the card... so blue and gray (do need to match the logo colors).

Requirements
Must have
• Would like the card to be sleek, modern and easy to ready

```html
<!DOCTYPE html>
<html lang="en">
<head>
<meta charset="utf-8">
<title>Varneck Bidding – Business Cards</title>
<link rel="stylesheet" href="https://fonts.googleapis.com/css2?family=Exo+2:wght@700&family=Open+Sans:wght@400;600&display=swap">
<style>
  :root {
    --brand-blue: #2b77b8;
    --brand-blue-light: #3a86c8;
    --brand-blue-deep: #2465a8;
    --brand-gray: #555759;
    --ink-gray: #45474a;
    --paper: #ffffff;
    --backdrop: #1f1f21;
  }
  * { margin: 0; padding: 0; box-sizing: border-box; }
  html, body {
    width: 1200px; height: 960px; overflow: hidden;
    background: var(--backdrop);
  }
  .sheet {
    position: relative; width: 1200px; height: 960px;
    display: flex; flex-direction: column; align-items: center; justify-content: center;
    gap: 60px;
  }
  .card {
    position: relative; width: 630px; height: 360px; overflow: hidden;
    border-radius: 4px;
  }

  /* Back side */
  .card-back {
    background: var(--brand-blue);
    color: var(--paper);
    display: flex; flex-direction: column; align-items: center; justify-content: center;
    gap: 22px;
  }
  .card-back .brand-name {
    font-family: "Exo 2", sans-serif; font-weight: 700;
    font-size: 54px; letter-spacing: 1px; text-transform: uppercase;
    color: var(--paper); line-height: 1;
  }
  .card-back .tagline {
    font-family: "Exo 2", sans-serif; font-weight: 700;
    font-size: 17px; letter-spacing: 1.5px; text-transform: uppercase;
    color: var(--paper);
  }

  /* Front side */
  .card-front { background: var(--paper); }
  .card-front .wave { position: absolute; inset: 0; width: 100%; height: 100%; }
  .card-front .brand-name {
    position: absolute; left: 38px; top: 58px;
    font-family: "Exo 2", sans-serif; font-weight: 700;
    font-size: 34px; line-height: 1.05; text-transform: uppercase;
    color: var(--brand-blue);
  }
  .contact {
    position: absolute; right: 34px; top: 146px;
    text-align: right; color: var(--paper);
    font-family: "Open Sans", sans-serif; font-size: 15px; line-height: 1.5;
  }
  .contact .person-name {
    font-family: "Exo 2", sans-serif; font-weight: 700;
    font-size: 22px; letter-spacing: 1px; text-transform: uppercase; line-height: 1.2;
  }
  .contact .person-role { text-transform: uppercase; font-size: 15px; margin-bottom: 4px; }
  .contact .address { margin-bottom: 4px; }
  .contact-line { display: flex; justify-content: flex-end; align-items: center; gap: 7px; }
  .contact-line svg { width: 13px; height: 13px; flex: none; }
</style>
</head>
<body>
<main class="sheet">

  <section class="card card-back" aria-label="Card back">
    <div class="brand-name">Varneck Bidding</div>
    <div class="tagline">Improving charity auctions nationwide</div>
  </section>

  <section class="card card-front" aria-label="Card front">
    <svg class="wave" viewBox="0 0 630 360" preserveAspectRatio="none" aria-hidden="true">
      <path d="M372 0 C352 120 320 230 150 360 L630 360 L630 0 Z" fill="var(--brand-gray)"/>
      <path d="M398 0 C380 130 350 240 190 360 L630 360 L630 0 Z" fill="var(--brand-blue-deep)"/>
      <path d="M404 0 C388 135 362 250 230 360 L630 360 L630 0 Z" fill="var(--brand-blue)"/>
    </svg>

    <div class="brand-name">Varneck<br>Bidding</div>

    <div class="contact">
      <div class="person-name">Marlon Teague</div>
      <div class="person-role">Owner/President</div>
      <div class="address">Street Name, City Name<br>Zipcode-012345</div>
      <div class="contact-line">555-301-7742
        <svg viewBox="0 0 16 16"><circle cx="8" cy="8" r="7.5" fill="#fff"/><path d="M5 4.2l1.6-.4 1 2.2-1 .8a5 5 0 0 0 2.6 2.6l.8-1 2.2 1-.4 1.6c-3.8.2-7-3-6.8-6.8z" fill="var(--brand-blue)"/></svg>
      </div>
      <div class="contact-line">hello@varneckbidding.com
        <svg viewBox="0 0 16 16"><rect x="1" y="3.5" width="14" height="9" rx="1" fill="#fff"/><path d="M1.5 4l6.5 5 6.5-5" fill="none" stroke="var(--brand-blue)" stroke-width="1.3"/></svg>
      </div>
      <div class="contact-line">www.bidharborhq.com
        <svg viewBox="0 0 16 16" fill="none" stroke="#fff" stroke-width="1.2"><circle cx="8" cy="8" r="6.5"/><ellipse cx="8" cy="8" rx="3" ry="6.5"/><path d="M1.5 8h13M2.5 4.8h11M2.5 11.2h11"/></svg>
      </div>
    </div>
  </section>

</main>
</body>
</html>
```